Redo a PPT pres. - Real Estate in Brazil - Socially equitable investments in Social Housing

We need to redo the presentation attached. It is an institutional presentation to attract local and foreign investors to invest in Brazilian Social Housing Projects structured by our company "TRV".
A middle class of 100 million, a housing deficit of 9M, a strong political will & positive income generation trends constitute grounds for a significant demand in social housing.
This make a perfect scheme for investors to invest in Brazilian Social Housing.
"TRV", is a consulting "boutique" focused in Brazilian real estate, specialized in structuring, analyzing and originating Brazilian social housing projects.
TRV is part of the group TRQ. TRQ is structured to create value through each step of the residential real estate business - structuring, financing, sales, marketing and technology.
We would like to see designs that use mainly the color blue. The final design should communicate financial safety and professionalism. In order to reach our needs, the designer will need to have basic understanding of finance and investment in order to highlight the most important information.
The idea is to receive back the PPT with each page redesigned and an homogeneous identity.
To all designers,
Target Market(s)
Institutional Investors and wealthy individuals
Industry/Entity Type
Residential
Look and feel
Each slider illustrates characteristics of the customer's brand and the style your logo design should communicate.

```html
<!DOCTYPE html>
<html lang="en">
<head>
<meta charset="utf-8">
<title>Macro-Environment &amp; Mortgage Market — Social Housing in Brazil</title>
<link rel="stylesheet" href="https://fonts.googleapis.com/css2?family=Tinos:wght@700&family=Open+Sans:wght@600;700;800&display=swap">
<style>
  :root {
    --navy: #0b2559;
    --navy-deep: #071a45;
    --accent-line: #2f7fd1;
    --cyan: #35c3f0;
    --sky-text: #4aa8ee;
    --page: #e9f0f8;
    --page-light: #f4f7fb;
    --subtext: #3a3d42;
    --white: #ffffff;
  }
  html, body {
    margin: 0;
    padding: 0;
    width: 1200px;
    height: 900px;
    overflow: hidden;
    background: var(--page);
  }
  .slide {
    position: relative;
    width: 1200px;
    height: 900px;
    overflow: hidden;
    font-family: "Open Sans", Arial, sans-serif;
  }
  .backdrop {
    position: absolute;
    inset: 0;
    background: linear-gradient(100deg, #dfe7f1 0%, #edf2f8 35%, var(--page-light) 65%, #e6edf6 100%);
  }
  .header {
    position: absolute;
    left: 0; top: 0;
    width: 1200px; height: 132px;
    background: linear-gradient(90deg, var(--navy-deep) 0%, var(--navy) 60%, #123a7a 100%);
    border-bottom: 4px solid var(--accent-line);
  }
  .header-skyline {
    position: absolute;
    right: 0; top: 0;
    width: 360px; height: 132px;
    background: linear-gradient(90deg, rgba(18,58,122,0) 0%, #2a5f9f 45%, #3f77b3 70%, #1d4d8c 100%);
  }
  .slide-title {
    position: absolute;
    left: 27px; top: 52px;
    margin: 0;
    font-family: "Tinos", "Times New Roman", serif;
    font-weight: 700;
    font-size: 34px;
    line-height: 1;
    letter-spacing: 0.3px;
    color: var(--white);
    white-space: nowrap;
  }
  .subtitle-band {
    position: absolute;
    left: 0; top: 136px;
    width: 760px; height: 70px;
    background: linear-gradient(90deg, rgba(255,255,255,0.85) 0%, rgba(255,255,255,0.6) 60%, rgba(255,255,255,0) 100%);
    border-bottom: 2px solid rgba(150,160,175,0.45);
    box-shadow: 0 6px 10px -6px rgba(80,90,110,0.35);
  }
  .subtitle {
    position: absolute;
    left: 30px; top: 158px;
    margin: 0;
    font-weight: 700;
    font-size: 31px;
    line-height: 1;
    color: var(--subtext);
  }
  .dial {
    position: absolute;
    left: 438px; top: 322px;
    width: 300px; height: 300px;
  }
  .dial-label {
    position: absolute;
    left: 486px; top: 404px;
    width: 204px;
    text-align: center;
    color: var(--white);
  }
  .dial-number {
    display: block;
    font-weight: 800;
    font-size: 88px;
    line-height: 1;
  }
  .dial-caption {
    display: block;
    margin-top: 8px;
    font-weight: 700;
    font-size: 24px;
    line-height: 1;
  }
  .footer-wave {
    position: absolute;
    left: 0; top: 0;
    width: 1200px; height: 900px;
  }
  .brand-name {
    position: absolute;
    left: 30px; top: 780px;
    margin: 0;
    font-family: "Tinos", "Times New Roman", serif;
    font-weight: 700;
    font-size: 84px;
    line-height: 1;
    color: var(--white);
  }
  .page-number {
    position: absolute;
    left: 1112px; top: 745px;
    width: 50px; height: 50px;
    border-radius: 50%;
    border: 2px solid #3c63a6;
    background: var(--navy);
    color: var(--white);
    font-weight: 700;
    font-size: 22px;
    line-height: 46px;
    text-align: center;
    box-sizing: border-box;
  }
  .deck-title {
    position: absolute;
    right: 28px; top: 830px;
    margin: 0;
    font-weight: 700;
    font-size: 36px;
    line-height: 1;
    letter-spacing: 0.5px;
    color: var(--sky-text);
    white-space: nowrap;
  }
</style>
</head>
<body>
<main class="slide">
  <div class="backdrop" role="img" aria-label="Faint photograph of glass office towers"></div>

  <header class="header">
    <div class="header-skyline" role="img" aria-label="Photograph of blue glass skyscrapers"></div>
    <h1 class="slide-title">MACRO-ENVIRONMENT &amp; MORTGAGE MARKET</h1>
  </header>

  <div class="subtitle-band"></div>
  <p class="subtitle">Investment signal</p>

  <svg class="dial" viewBox="0 0 300 300" aria-hidden="true">
    <defs>
      <radialGradient id="ring-grey" cx="50%" cy="45%" r="55%">
        <stop offset="0%" stop-color="#e4e6e9"/>
        <stop offset="100%" stop-color="#b7bbc1"/>
      </radialGradient>
      <radialGradient id="ring-dark" cx="50%" cy="40%" r="60%">
        <stop offset="0%" stop-color="#55585c"/>
        <stop offset="100%" stop-color="#2b2d30"/>
      </radialGradient>
      <linearGradient id="dial-face" x1="0" y1="1" x2="1" y2="0">
        <stop offset="0%" stop-color="#1160c9"/>
        <stop offset="100%" stop-color="#3cc0f8"/>
      </linearGradient>
    </defs>
    <circle cx="150" cy="150" r="148" fill="url(#ring-grey)"/>
    <circle cx="150" cy="150" r="132" fill="url(#ring-dark)"/>
    <circle cx="150" cy="150" r="104" fill="#0a1b3a"/>
    <circle cx="150" cy="150" r="100" fill="url(#dial-face)"/>
  </svg>
  <div class="dial-label">
    <span class="dial-number">1</span>
    <span class="dial-caption">GREEN LIGHT</span>
  </div>

  <svg class="footer-wave" viewBox="0 0 1200 900" aria-hidden="true">
    <defs>
      <linearGradient id="wave-fill" x1="0" y1="0" x2="0" y2="1">
        <stop offset="0%" stop-color="#0f2f6d"/>
        <stop offset="100%" stop-color="#071a45"/>
      </linearGradient>
    </defs>
    <path d="M0,668 C260,790 760,820 1200,668 L1200,900 L0,900 Z" fill="url(#wave-fill)"/>
    <path d="M0,668 C260,790 760,820 1200,668" fill="none" stroke="var(--cyan)" stroke-width="3"/>
  </svg>

  <p class="brand-name">TRV</p>
  <div class="page-number">02</div>
  <p class="deck-title">SOCIAL HOUSING IN BRAZIL</p>
</main>
</body>
</html>
```